Painting Company Business Card

Brightwell Painting needs a new business card. See attachments for our logo and current card as an example.
We want to utilize the same colors in the logo, and keep all the information that is currently on it. Just need an updated and modern design.
We are open to loosing the Association Logos if it means a better design.
We are also entertaining a spot for a picture of a headshot of the person listed on the card. Head shot can be finished later.

```html
<!DOCTYPE html>
<html lang="en">
<head>
<meta charset="utf-8">
<title>Brightwell Painting – Business Card</title>
<link rel="stylesheet" href="https://fonts.googleapis.com/css2?family=Jost:wght@400;500;600&display=swap">
<style>
  :root {
    --stage: #2a2a2a;
    --card-white: #ffffff;
    --olive: #3f4731;
    --maroon: #6b3a36;
    --ink: #3a3a3a;
  }
  * { margin: 0; padding: 0; box-sizing: border-box; }
  html, body {
    width: 1125px; height: 1200px; overflow: hidden;
    background: var(--stage);
    font-family: "Jost", "Futura", sans-serif;
  }
  .card {
    position: absolute; left: 156px;
    width: 825px; height: 471px;
    border-radius: 26px; overflow: hidden;
  }
  .card--front { top: 106px; background: var(--card-white); }
  .card--back { top: 639px; background: var(--olive); }

  .top-band {
    position: absolute; left: 0; top: 20px;
    width: 800px; height: 40px;
    background: var(--olive);
    border-top-right-radius: 18px;
  }

  .wordmark {
    position: absolute; left: 48px; top: 92px;
    color: var(--olive); font-weight: 600;
    font-size: 46px; line-height: 1.0; letter-spacing: -0.5px;
  }

  .holder { position: absolute; left: 48px; top: 262px; }
  .holder__name {
    color: var(--olive); font-weight: 600; font-size: 32px;
    font-variant: small-caps; letter-spacing: 0.3px; line-height: 1.1;
  }
  .holder__title { color: var(--maroon); font-size: 21px; margin-top: 2px; }

  .contacts { position: absolute; left: 48px; top: 346px; list-style: none; }
  .contacts li {
    display: flex; align-items: center; gap: 10px;
    height: 27px; font-size: 19.5px; color: var(--ink);
  }
  .contacts svg { width: 17px; height: 17px; fill: var(--ink); }

  .services {
    position: absolute; right: 139px; top: 346px;
    list-style: none; text-align: right;
    font-size: 19.5px; color: var(--ink); line-height: 25px;
  }
  .services .dot {
    display: inline-block; width: 8px; height: 8px; border-radius: 50%;
    background: var(--ink); margin: 0 4px 3px 8px; vertical-align: middle;
  }

  .back-wordmark {
    position: absolute; left: 0; right: 0; top: 180px;
    text-align: center; color: var(--card-white);
    font-weight: 600; font-size: 58px; line-height: 1.05;
  }
</style>
</head>
<body>
  <section class="card card--front" aria-label="Business card front">
    <div class="top-band"></div>

    <div class="wordmark">Brightwell<br>Painting</div>

    <div class="holder">
      <p class="holder__name">Daniel Harper</p>
      <p class="holder__title">Quality Manager</p>
    </div>

    <ul class="contacts">
      <li>
        <svg viewBox="0 0 24 24" aria-hidden="true"><path d="M6.6 10.8a15.1 15.1 0 0 0 6.6 6.6l2.2-2.2a1 1 0 0 1 1-.25 11.4 11.4 0 0 0 3.6.57 1 1 0 0 1 1 1V20a1 1 0 0 1-1 1A17 17 0 0 1 3 4a1 1 0 0 1 1-1h3.5a1 1 0 0 1 1 1c0 1.25.2 2.45.57 3.57a1 1 0 0 1-.25 1z"/></svg>
        262-555-0148
      </li>
      <li>
        <svg viewBox="0 0 24 24" aria-hidden="true"><path d="M2 5h20v14H2z M4 7v.5l8 5 8-5V7l-8 5z" fill-rule="evenodd"/></svg>
        daniel@brightwellpainting.com
      </li>
      <li>
        <svg viewBox="0 0 24 24" aria-hidden="true"><path d="M12 2a10 10 0 1 0 0 20 10 10 0 0 0 0-20zm-1 17.9A8 8 0 0 1 4.2 10.2L9 15v1a2 2 0 0 0 2 2zm6.9-2.5A2 2 0 0 0 16 16h-1v-3a1 1 0 0 0-1-1H8v-2h2a1 1 0 0 0 1-1V7h2a2 2 0 0 0 2-2v-.4a8 8 0 0 1 2.9 12.8z"/></svg>
        brightwellpainting.com
      </li>
    </ul>

    <ul class="services">
      <li>Exterior Painting<span class="dot"></span></li>
      <li>Interior Painting<span class="dot"></span></li>
      <li>Carpentry<span class="dot"></span>Drywell<span class="dot"></span></li>
    </ul>
  </section>

  <section class="card card--back" aria-label="Business card back">
    <div class="back-wordmark">Brightwell<br>Painting</div>
  </section>
</body>
</html>
```